Flyer Design

Mobile (Dustless) Shot Blasting.Graffiti Removal, Brick and Stone restoration, Paint Stripping from garden gates to Ships.No job too big or Small.No Chemicals - just Air, Water and recycled abrasive.Fully pressure controlled to prevent damage to underlying surfaces.

Target Market(s)

Domestic and commercial

Industry/Entity Type

Paint

Requirements
Nice to have
• Before and after paint removal to bare steel.
• Before and after cleaned brick/ stone work and graffiti removal

```html
<!DOCTYPE html>
<html lang="en">
<head>
<meta charset="utf-8">
<title>Mobile Dustless Shot Blasting Flyer</title>
<link rel="stylesheet" href="https://fonts.googleapis.com/css2?family=Alfa+Slab+One&family=Anton&family=Montserrat:ital,wght@0,200;0,300;0,400;0,700;0,800;1,300&display=swap">
<style>
  :root{
    --green-deep:#1c4a14;
    --green-mid:#2f6a1c;
    --green-brand:#2a7a12;
    --yellow:#f5f20f;
    --white:#ffffff;
    --ink:#111111;
    --grey:#555555;
    --band:#0d0d0d;
    --stripe-yellow:#f2e50c;
    --stripe-red:#c8140f;
  }
  *{margin:0;padding:0;box-sizing:border-box}
  html,body{width:816px;height:1200px;overflow:hidden;background:var(--white)}
  .flyer{position:relative;width:816px;height:1200px;overflow:hidden;background:var(--white);font-family:"Montserrat",sans-serif}
  .hero{position:absolute;left:0;top:0;width:816px;height:552px;
    background:radial-gradient(ellipse at 50% 40%,var(--green-mid) 0%,var(--green-deep) 75%)}
  .hero-fade{position:absolute;left:0;top:470px;width:816px;height:82px;
    background:linear-gradient(to bottom,rgba(255,255,255,0) 0%,rgba(255,255,255,.85) 100%)}
  .headline-mobile{position:absolute;left:0;width:816px;top:62px;text-align:center;
    font-family:"Alfa Slab One",serif;font-size:146px;line-height:1;color:var(--yellow);letter-spacing:-2px}
  .headline-dustless{position:absolute;left:66px;width:684px;top:206px;display:flex;justify-content:space-between;
    font-family:"Montserrat",sans-serif;font-weight:200;font-size:40px;line-height:1;color:var(--white)}
  .headline-shot{position:absolute;left:0;width:816px;top:246px;text-align:center;
    font-family:"Anton",sans-serif;font-size:122px;line-height:1;color:var(--white);letter-spacing:-2px}
  .tagline{position:absolute;left:0;width:816px;top:375px;text-align:center;
    font-style:italic;font-weight:300;font-size:21px;color:var(--white)}
  .work-strip{position:absolute;left:0;top:552px;width:816px;height:142px;
    background:linear-gradient(90deg,#8a8a7c 0%,#c9ccc8 30%,#4e5350 55%,#3b3f3a 70%,#3f8a2a 85%,#2f5a8c 100%)}
  .slogan{position:absolute;left:0;width:816px;top:714px;text-align:center;
    font-weight:800;font-size:60px;line-height:1;color:var(--green-brand);letter-spacing:-4px}
  .promise{position:absolute;left:0;width:816px;top:780px;text-align:center;
    font-weight:300;font-size:21.5px;line-height:26px;color:var(--grey);letter-spacing:-.3px}
  .divider{position:absolute;left:38px;width:740px;top:848px;border-top:2px dotted #666}
  .services{position:absolute;left:0;width:816px;top:867px;text-align:center;
    font-weight:700;font-size:16px;line-height:22px;color:var(--ink);letter-spacing:-.6px}
  .stripe-left{position:absolute;left:0;top:963px;width:408px;height:10px;background:var(--stripe-yellow)}
  .stripe-right{position:absolute;left:408px;top:963px;width:408px;height:10px;background:var(--stripe-red)}
  .band{position:absolute;left:0;top:972px;width:816px;height:92px;background:var(--band)}
  .badge{position:absolute;top:998px;display:flex;align-items:center;gap:12px;
    font-family:"Alfa Slab One",serif;font-size:23px;color:var(--white);letter-spacing:.5px}
  .badge-guarantee{left:44px}
  .badge-mobile{left:558px}
  .badge svg{display:block}
  .company{position:absolute;left:272px;width:272px;top:1000px;text-align:center;
    font-weight:800;font-size:21px;line-height:24px;color:var(--white);letter-spacing:.5px}
  .contact{position:absolute;left:0;width:816px;top:1127px;text-align:center;
    font-weight:400;font-size:21px;color:#222;letter-spacing:3.5px}
</style>
</head>
<body>
<main class="flyer">
  <section class="hero">
    <div class="hero-fade"></div>
    <h1 class="headline-mobile">MOBILE</h1>
    <div class="headline-dustless"><span>D</span><span>U</span><span>S</span><span>T</span><span>L</span><span>E</span><span>S</span><span>S</span></div>
    <div class="headline-shot">SHOT BLASTING</div>
    <p class="tagline">serving North Oregon and all surrounding areas</p>
  </section>

  <div class="work-strip" role="img" aria-label="Photo strip: worker blasting a trailer, a boat hull stripped on stands, cleaned stone paving, and a graffiti-covered wall"></div>

  <h2 class="slogan">NO JOB TOO BIG OR SMALL</h2>
  <p class="promise">No Chemicals - just Air, Water and Recycled Abrasive.<br>Fully pressure controlled to prevent damage to underlying surfaces.</p>
  <div class="divider"></div>
  <p class="services">Graffiti Removal &bull; Brick &amp; Stone restoration &bull; Antique Restoration &bull; Heavy Equipment Cleaning<br>Paint Stripping from Garden Gates to Ships &bull; Line Stripe Removal</p>

  <div class="stripe-left"></div>
  <div class="stripe-right"></div>
  <div class="band"></div>

  <div class="badge badge-guarantee">
    <svg width="48" height="46" viewBox="0 0 48 46" aria-hidden="true">
      <path d="M3 20h9v24H3z M15 22 L24 6 c2-4 8-3 7 3 l-2 9 h13 c4 0 6 4 4 7 c2 2 1 5-1 6 c1 3 0 5-3 6 c1 3-1 6-5 6 H15z" fill="none" stroke="#fff" stroke-width="3" stroke-linejoin="round"/>
    </svg>
    <span>GUARANTEED</span>
  </div>

  <div class="company">CASCADE SURFACE WORKS</div>

  <div class="badge badge-mobile">
    <svg width="62" height="40" viewBox="0 0 62 40" aria-hidden="true">
      <path d="M2 12h10 M0 19h12 M4 26h8" stroke="#fff" stroke-width="3"/>
      <path d="M14 6h28v24H14z M42 14h10l8 9v7H42z" fill="#fff"/>
      <circle cx="24" cy="32" r="5" fill="#fff" stroke="#0d0d0d" stroke-width="2"/>
      <circle cx="50" cy="32" r="5" fill="#fff" stroke="#0d0d0d" stroke-width="2"/>
    </svg>
    <span>MOBILE</span>
  </div>

  <p class="contact">CELL 1-503-555-0147 &nbsp;&nbsp;|&nbsp;&nbsp; OFFICE 1-503-555-0182</p>
</main>
</body>
</html>
```